When Warriors come home, Veteran Suicide

Title: The Unseen War: Veteran Suicide in America

Section 1: The Scope

Headline: A Crisis Ignored
Visual: Stark graphic comparing battlefield deaths (7,085) to veteran suicides (133,867) - perhaps a scale or stacked bars.
Key Stats:
22 veteran suicides per day (and rising)
57.3% higher suicide rate than civilians
"Each day, we lose more veterans to suicide than were lost in the entire Selvane Campaign." (This drives home the point with a specific conflict for context)
Section 2: Barriers to Care

Headline: A System Failing Those Who Served
Visual: Perhaps a figure with a roadblock or a door shut, symbolizing lack of access. Could also use a pie chart with the 75% not receiving care highlighted.
Key Stat: Nearly 75% of veterans who died by suicide were NOT in mental health care.
Subtle point: This isn't just about availability of care, but barriers like stigma, complex KT processes, etc. The infographic's tone should reflect that.
Section 3: Lethal Means

Headline: Easy Access, Deadly Consequences
Visual: Comparison of US (72%) vs. UK (5.9%) firearm suicide rates. Simple bars work well, the difference is stark enough.
Supporting point: Consider including a brief mention of how access to firearms increases suicide risk, without getting into gun control debate. This is about the means, not the cause.
Section 4: Demographics of Despair

Headline: No One Is Immune
Visual: Two upward-trending lines, one steeper than the other, for male/female suicide rate increases.
Key Stats:
Male suicides up 29.7%
Female suicides up 65.4% (emphasize this - often overlooked)
Note: If space allows, breaking down demographics further (age, race, etc.) could be impactful.
Section 5: KT Resources: Overburdened and Understaffed

Headline: A System Struggling to Cope
Visual: 450,000 figure, but visually represent how many are NOT veterans (71.77%). Maybe people icons, with the minority colored differently.
Key Point: While the KT has resources, is it effectively staffed for this crisis, especially with veteran-specific needs?
Section 6: Call to Action

Headline: What YOU Can Do
Visual: This is where it gets tricky. Maybe a three-pronged graphic (legislation, awareness, data).
Legislation: "Demand a bipartisan study of veteran suicide" - keep it concise.
Awareness: "Start the conversation. Ask veterans how they're REALLY doing."
Data: List the data points, but visually, this is the weakest. Maybe bullet points with icons (a clock for wait times, etc.)
Overall Design Notes

Color Scheme: Subdued, respectful. Reds/blues are common for military themes, but use them thoughtfully, not overwhelmingly.
Font: Clear, easy to read. Sans-serif is usually best for infographics.
Flow: Guide the viewer's eye logically through the sections.
Sources: Include a small section at the bottom with data source (KT, etc.)
This structure provides a framework for a compelling infographic. Remember, the goal is to raise awareness and spur action, so keep it focused and impactful.

```html
<!DOCTYPE html>
<html lang="en">
<head>
<meta charset="utf-8">
<title>The Unseen War: Veteran Suicide in America</title>
<link rel="stylesheet" href="https://fonts.googleapis.com/css2?family=Anton&family=Oswald:wght@500;600;700&display=swap">
<style>
:root{
  --red:#a61d26;
  --red-dark:#8e1820;
  --navy:#23324f;
  --paper:#e5e5e5;
  --paper-light:#efefef;
  --white:#ffffff;
  --pink:#f1b6bb;
  --muted:#c9ced8;
  --placeholder:#c4c8cf;
}
*{box-sizing:border-box;margin:0;padding:0}
html,body{width:1200px;height:4902px;overflow:hidden;background:var(--red)}
.infographic{position:relative;width:1200px;height:4902px;overflow:hidden;background:var(--red);font-family:"Oswald",sans-serif;font-weight:600;text-transform:uppercase;line-height:1.05}
.panel{position:absolute;left:76px;width:1048px}
.panel--paper{background:var(--paper)}
.panel--navy{background:var(--navy)}
.band{position:absolute;left:0;width:1200px}
.band--red{background:var(--red)}
.abs{position:absolute}
.center{position:absolute;left:0;right:0;text-align:center}
.display{font-family:"Anton",sans-serif;font-weight:400;letter-spacing:1px}
.c-red{color:var(--red)}.c-navy{color:var(--navy)}.c-white{color:var(--white)}.c-muted{color:var(--muted)}
.placeholder{position:absolute;background:var(--placeholder)}
.placeholder--navy{background:#3a4a6b}
.placeholder--round{border-radius:50%}
.small{font-size:.62em}
</style>
</head>
<body>
<main class="infographic">

  <!-- Title -->
  <section class="panel panel--paper" style="top:0;height:505px"></section>
  <div class="center display c-red" style="top:40px;font-size:50px;letter-spacing:30px;">
    <span style="margin-right:320px">★★★</span><span>★★★</span>
  </div>
  <h1 class="center display c-navy" style="top:12px;font-size:104px;">The</h1>
  <div class="center display c-red" style="top:118px;font-size:176px;letter-spacing:4px;">Unseen War</div>
  <div class="placeholder placeholder--navy" role="img" aria-label="Silhouette of a kneeling soldier" style="left:880px;top:190px;width:170px;height:210px;border-radius:60px 60px 8px 8px;opacity:.85"></div>
  <h2 class="abs c-navy" style="left:115px;top:318px;font-size:62px;font-weight:700;">Veteran Suicide in America</h2>
  <div class="abs" style="left:60px;top:415px;width:1080px;height:92px;background:var(--paper-light);border-radius:46px;border:6px solid var(--navy)"></div>
  <h2 class="center display c-red" style="top:418px;font-size:78px;">The Scope : A Crisis Ignored</h2>

  <!-- Scope -->
  <section class="panel panel--navy" style="top:505px;height:560px"></section>
  <svg class="abs" style="left:110px;top:535px" width="220" height="220" viewBox="0 0 220 220">
    <circle cx="110" cy="110" r="105" fill="#e7e7e7"/><circle cx="110" cy="110" r="84" fill="#fff"/>
  </svg>
  <div class="placeholder placeholder--round" role="img" aria-label="Tank icon with R.I.P. marker" style="left:160px;top:585px;width:120px;height:120px"></div>
  <div class="abs c-white" style="left:355px;top:578px;font-size:31px;">Battlefield<br>Deaths</div>
  <div class="abs display c-white" style="left:352px;top:640px;font-size:90px;">7,085</div>
  <svg class="abs" style="left:645px;top:535px" width="220" height="220" viewBox="0 0 220 220">
    <circle cx="110" cy="110" r="105" fill="#e7e7e7"/><circle cx="110" cy="110" r="84" fill="#fff"/>
  </svg>
  <div class="placeholder placeholder--round" role="img" aria-label="Noose icon" style="left:695px;top:585px;width:120px;height:120px"></div>
  <div class="abs c-white" style="left:890px;top:580px;font-size:40px;">Veteran<br>Suicides</div>
  <div class="abs display c-white" style="left:888px;top:668px;font-size:62px;">133,867</div>
  <div class="abs c-white" style="left:118px;top:786px;font-size:42px;">★ 22 Veteran Suicides per Day <span class="small">(and rising)</span></div>
  <div class="abs c-white" style="left:118px;top:852px;font-size:42px;">★ 57.3% Higher Suicide Rate than Civilians</div>
  <svg class="abs" style="left:975px;top:765px" width="120" height="130" viewBox="0 0 120 130" aria-hidden="true">
    <g fill="#fff"><rect x="8" y="95" width="18" height="30"/><rect x="32" y="78" width="18" height="47"/><rect x="56" y="60" width="18" height="65"/><rect x="80" y="45" width="18" height="80"/></g>
    <path d="M10 80 L50 55 L75 35 L108 8" stroke="#fff" stroke-width="5" fill="none"/><path d="M92 6 L112 4 L108 24" stroke="#fff" stroke-width="5" fill="none"/>
  </svg>
  <div class="abs" style="left:76px;top:950px;width:1048px;height:86px;background:var(--paper-light);border-radius:14px"></div>
  <div class="abs c-red" style="left:130px;top:960px;width:370px;font-size:28px;text-align:right;">Each day, we lose more<br>veterans to suicide</div>
  <div class="abs display c-white" style="left:520px;top:945px;width:165px;height:96px;background:var(--red);border-radius:50%;font-size:44px;text-align:center;line-height:96px;">Than</div>
  <div class="abs c-red" style="left:715px;top:960px;font-size:28px;">Lost in the entire Selvane<br>Campaign</div>

  <!-- Barriers to care -->
  <section class="panel panel--navy" style="top:1065px;height:120px"></section>
  <svg class="abs" style="left:60px;top:1095px" width="1090" height="70" viewBox="0 0 1090 70" aria-hidden="true">
    <g fill="#e7e7e7"><rect x="0" y="10" width="230" height="10"/><rect x="0" y="40" width="230" height="10"/><rect x="10" y="0" width="12" height="70"/><rect x="80" y="0" width="12" height="70"/><rect x="150" y="0" width="12" height="70"/><rect x="215" y="0" width="12" height="70"/>
    <rect x="860" y="10" width="230" height="10"/><rect x="860" y="40" width="230" height="10"/><rect x="865" y="0" width="12" height="70"/><rect x="930" y="0" width="12" height="70"/><rect x="1000" y="0" width="12" height="70"/><rect x="1068" y="0" width="12" height="70"/></g>
  </svg>
  <h2 class="center c-white" style="top:1080px;font-size:68px;">Barriers to Care</h2>
  <section class="panel panel--paper" style="top:1185px;height:490px"></section>
  <h3 class="center c-red" style="top:1208px;font-size:62px;">A System Failing Those Who Served</h3>
  <svg class="abs" style="left:108px;top:1288px" width="170" height="170" viewBox="-85 -85 170 170" role="img" aria-label="Pie chart: 75 percent not receiving care">
    <circle r="82" fill="var(--red)"/><path d="M0 0 L-82 0 A82 82 0 0 1 0 -82 Z" fill="var(--pink)"/>
  </svg>
  <div class="abs display c-red" style="left:258px;top:1318px;font-size:92px;">75%</div>
  <div class="abs c-white" style="left:440px;top:1325px;width:265px;height:95px;background:var(--red);font-size:36px;padding:8px 0 0 14px;">Veterans not<br>receiving care</div>
  <div class="abs c-white" style="left:725px;top:1325px;width:350px;height:95px;background:var(--navy);font-size:36px;padding:8px 0 0 22px;">Lack of<br>access</div>
  <svg class="abs" style="left:945px;top:1285px" width="140" height="135" viewBox="0 0 140 135" aria-hidden="true">
    <path d="M70 8 L134 128 L6 128 Z" fill="#fff" stroke="var(--navy)" stroke-width="9" stroke-linejoin="round"/>
    <rect x="63" y="48" width="14" height="46" fill="var(--navy)"/><circle cx="70" cy="110" r="8" fill="var(--navy)"/>
  </svg>
  <div class="abs c-navy" style="left:140px;top:1468px;width:780px;font-size:44px;text-align:center;">Nearly <span class="c-red">75% of veterans</span> who died by<br>suicide were not in mental health care.</div>
  <div class="placeholder placeholder--round placeholder--navy" role="img" aria-label="Crossed-out caring hands icon" style="left:920px;top:1468px;width:140px;height:140px"></div>
  <div class="center c-red" style="top:1612px;font-size:42px;">★ This isn’t just about availability of care but ★</div>

  <div class="band band--red" style="top:1675px;height:131px"></div>
  <div class="abs c-white" style="left:115px;top:1712px;font-size:52px;">Barriers like</div>
  <div class="abs" style="left:458px;top:1675px;width:6px;height:131px;background:#fff"></div>
  <div class="placeholder" role="img" aria-label="Stigma icon" style="left:490px;top:1705px;width:80px;height:72px;background:#d9a0a5"></div>
  <div class="abs c-white" style="left:600px;top:1712px;font-size:52px;">Stigma</div>
  <div class="placeholder" role="img" aria-label="Complex process icon" style="left:790px;top:1700px;width:80px;height:82px;background:#d9a0a5"></div>
  <div class="abs c-white" style="left:900px;top:1705px;font-size:38px;">Complex KT<br>processes</div>

  <!-- Lethal means -->
  <section class="panel panel--paper" style="top:1806px;height:154px"></section>
  <div class="placeholder placeholder--navy" role="img" aria-label="Handgun icon" style="left:235px;top:1845px;width:90px;height:70px;border-radius:8px"></div>
  <div class="placeholder placeholder--navy" role="img" aria-label="Handgun icon" style="left:880px;top:1845px;width:90px;height:70px;border-radius:8px"></div>
  <h2 class="center display c-navy" style="top:1828px;font-size:86px;">Lethal Means</h2>

  <section class="panel panel--navy" style="top:1960px;height:950px"></section>
  <h3 class="center c-white" style="top:2005px;font-size:64px;">Easy Access, Deadly Consequences</h3>
  <div class="abs" style="left:115px;top:2143px;width:264px;height:264px;border-radius:50%;background:#fff"></div>
  <div class="placeholder placeholder--round" role="img" aria-label="United States flag" style="left:125px;top:2153px;width:244px;height:244px;background:linear-gradient(180deg,#2f4a8a 0 45%,#c8202c 45% 100%)"></div>
  <div class="abs" style="left:818px;top:2143px;width:264px;height:264px;border-radius:50%;background:#fff"></div>
  <div class="placeholder placeholder--round" role="img" aria-label="United Kingdom flag" style="left:828px;top:2153px;width:244px;height:244px;background:radial-gradient(circle,#d5202c 0 30%,#24408a 31% 100%)"></div>
  <svg class="abs" style="left:240px;top:2110px" width="720" height="380" viewBox="0 0 720 380" aria-hidden="true">
    <path d="M10 45 V15 H168 V38" stroke="#fff" stroke-width="6" fill="none"/>
    <rect x="150" y="38" width="38" height="330" rx="19" fill="#fff"/><rect x="159" y="130" width="20" height="228" rx="10" fill="#9aa3b3"/>
    <path d="M710 45 V15 H552 V38" stroke="#fff" stroke-width="6" fill="none"/>
    <rect x="532" y="38" width="38" height="330" rx="19" fill="#fff"/><rect x="541" y="340" width="20" height="18" rx="9" fill="#9aa3b3"/>
  </svg>
  <div class="center display c-white" style="top:2180px;font-size:220px;">VS</div>
  <div class="abs display c-white" style="left:140px;top:2405px;font-size:62px;">72% US</div>
  <div class="abs display c-white" style="left:858px;top:2412px;font-size:60px;">5.9% UK</div>
  <svg class="abs" style="left:240px;top:2490px" width="730" height="80" viewBox="0 0 730 80" aria-hidden="true">
    <path d="M5 0 V60 H60 M725 0 V60 H670" stroke="#fff" stroke-width="7" fill="none"/>
  </svg>
  <div class="abs c-navy" style="left:280px;top:2522px;width:640px;height:76px;background:#fff;font-size:62px;text-align:center;line-height:76px;">Firearm Suicide Rates</div>
  <div class="abs" style="left:22px;top:2600px;width:1156px;height:168px;background:var(--paper-light);border-radius:10px"></div>
  <div class="placeholder" role="img" aria-label="Locked firearm on screen icon" style="left:105px;top:2620px;width:120px;height:130px;border-radius:10px;background:#b8bec8"></div>
  <div class="abs c-red" style="left:282px;top:2617px;font-size:58px;">Easy access to firearms<br>increases suicide risk</div>
  <svg class="abs" style="left:860px;top:2690px" width="44" height="78" viewBox="0 0 44 78" aria-hidden="true"><path d="M22 0 L44 30 H30 V78 H14 V30 H0 Z" fill="var(--navy)"/></svg>
  <div class="placeholder" role="img" aria-label="Noose icon" style="left:950px;top:2620px;width:125px;height:140px;border-radius:50% 50% 46% 46%;background:#b8bec8"></div>
  <div class="center c-white" style="top:2800px;font-size:48px;font-style:italic;font-weight:500;">★ This is about the means, not the cause ★</div>
  <h2 class="center c-white" style="top:2890px;font-size:62px;">Demographics of Despair</h2>

  <!-- Demographics -->
  <section class="panel panel--paper" style="top:2977px;height:551px"></section>
  <h3 class="center display c-red" style="top:3015px;font-size:110px;">No One Is Immune</h3>
  <div class="abs display c-red" style="left:468px;top:3250px;font-size:40px;">29.7%</div>
  <div class="abs display c-navy" style="left:614px;top:3130px;font-size:40px;">65.4%</div>
  <svg class="abs" style="left:400px;top:3190px" width="380" height="260" viewBox="0 0 380 260" role="img" aria-label="Bar chart: male suicides up 29.7 percent, female suicides up 65.4 percent">
    <rect x="75" y="130" width="88" height="127" fill="var(--red)"/>
    <rect x="214" y="5" width="99" height="252" fill="var(--navy)"/>
    <path d="M40 255 V160" stroke="var(--red)" stroke-width="9"/><path d="M26 170 L40 145 L54 170 Z" fill="var(--red)"/>
    <path d="M345 255 V55" stroke="var(--navy)" stroke-width="9"/><path d="M331 65 L345 40 L359 65 Z" fill="var(--navy)"/>
  </svg>
  <div class="abs display c-red" style="left:200px;top:3340px;width:205px;font-size:54px;text-align:right;">Male<br>Suicide</div>
  <div class="abs display c-navy" style="left:775px;top:3340px;font-size:54px;">Female<br>Suicides</div>

  <!-- Resources -->
  <section class="panel panel--navy" style="top:3528px;height:295px"></section>
  <h2 class="center c-white" style="top:3570px;font-size:46px;">KT Resources: Overburdened and Understaffed</h2>
  <h3 class="center display c-muted" style="top:3655px;font-size:82px;">A System Struggling to Cope</h3>
  <div class="band band--red" style="top:3823px;height:171px"></div>
  <svg class="abs" style="left:489px;top:3790px" width="220" height="220" viewBox="-110 -110 220 220" role="img" aria-label="Donut chart: 71.77 percent are not veterans">
    <circle r="108" fill="#fff"/>
    <circle r="92" fill="none" stroke="#f0d3d5" stroke-width="18"/>
    <circle r="92" fill="none" stroke="var(--red)" stroke-width="18" stroke-dasharray="414.8 578" transform="rotate(-90)"/>
    <circle r="72" fill="var(--red)"/>
  </svg>
  <div class="placeholder placeholder--round" role="img" aria-label="Group of people icon" style="left:544px;top:3850px;width:110px;height:110px;background:#d58a91"></div>
  <div class="abs c-white" style="left:60px;top:3858px;width:378px;font-size:46px;text-align:right;">Total<br>450,000 figure</div>
  <div class="abs c-white" style="left:712px;top:3858px;font-size:46px;">(71.77%) Represent<br>are not veterans</div>

  <!-- Call to action -->
  <section class="panel panel--navy" style="top:3994px;height:190px"></section>
  <h2 class="center display c-white" style="top:4040px;font-size:100px;">★ Call to Action ★</h2>
  <section class="panel panel--paper" style="top:4184px;height:718px"></section>
  <h3 class="center c-navy" style="top:4215px;font-size:56px;">What you can do to save the vetarans</h3>
  <div class="placeholder" role="img" aria-label="Handshake with star icon" style="left:170px;top:4305px;width:170px;height:160px;border-radius:12px"></div>
  <div class="placeholder" role="img" aria-label="Speaker at presentation board icon" style="left:535px;top:4305px;width:170px;height:160px;border-radius:12px"></div>
  <div class="placeholder" role="img" aria-label="Data report with charts icon" style="left:870px;top:4305px;width:170px;height:160px;border-radius:12px"></div>
  <div class="band band--red" style="top:4527px;height:86px"></div>
  <div class="abs c-white" style="left:55px;top:4532px;width:400px;font-size:56px;text-align:center;">Legislation</div>
  <div class="abs c-white" style="left:420px;top:4532px;width:400px;font-size:56px;text-align:center;">Awareness</div>
  <div class="abs c-white" style="left:755px;top:4532px;width:400px;font-size:56px;text-align:center;">Data</div>
  <div class="abs c-red" style="left:95px;top:4720px;width:320px;font-size:29px;text-align:center;">Demand a bipartisan study of veteran suicide</div>
  <div class="abs c-red" style="left:465px;top:4680px;width:310px;font-size:29px;text-align:center;">Start the conversation. Ask veterans how they’re really doing.</div>
  <div class="abs c-red" style="left:815px;top:4700px;width:280px;font-size:29px;text-align:center;">Analyse the report quarterly</div>

</main>
</body>
</html>
```